Bottle design for a range of water enhancers

We need a bottle designed for a new range of water enhancers manufactured by the company, Vemo Kettle based in Lahore, Pakistan. The product is called "Vemo" and comes in 6 different flavors/colors. In essence, Vemo is a zero sugar, zero calorie flavor concentrate that is squirted in a glass of water directly from the bottle to make a refreshing beverage. The bottle size is about 60 ml. The bottle needs to be stylish, unique and must have a premium/high-end look to it. The shape of the bottle must be relatively flat. The bottle must be able to translate in to different colors according to the flavor.Some potential sketches have been added for reference.

Target Market(s)

Target market has been identified between the ages of 18 to 35

Colors

Designer to choose colors to be used in the design.

Requirements
Must have
• a sleek, eye catching design.
Nice to have
• A transparent section of the bottle where you can see the liquid inside.
Should not have
• bulky shapes

```html
<!DOCTYPE html>
<html lang="en">
<head>
<meta charset="utf-8">
<title>Vemo Liquid Water Enhancer – Puply Kiwi Bottle</title>
<link href="https://fonts.googleapis.com/css2?family=Quicksand:wght@300;400;500;700&family=Great+Vibes&family=Oswald:wght@300&display=swap" rel="stylesheet">
<style>
  :root {
    --stage: #000000;
    --body-top: #3d3d3d;
    --body-bottom: #2c2c2c;
    --seam: #262626;
    --lime: #b3cf1f;
    --lime-light: #cfe55a;
    --lime-deep: #86a312;
    --kiwi-skin: #8a6a3c;
    --kiwi-flesh: #7fa82a;
    --ink-white: #ffffff;
  }
  html, body {
    margin: 0;
    padding: 0;
    width: 1200px;
    height: 900px;
    overflow: hidden;
    background: var(--stage);
  }
  .bottle-art {
    display: block;
    width: 1200px;
    height: 900px;
  }
  .claim-figure { font-family: "Quicksand", sans-serif; font-weight: 700; font-size: 17px; fill: var(--ink-white); }
  .claim-word { font-family: "Quicksand", sans-serif; font-weight: 500; font-size: 10px; fill: var(--ink-white); }
  .claim-sub { font-family: "Quicksand", sans-serif; font-weight: 500; font-size: 4.2px; letter-spacing: 1.2px; fill: var(--ink-white); }
  .brand-name { font-family: "Quicksand", sans-serif; font-weight: 400; font-size: 58px; letter-spacing: 4px; fill: var(--ink-white); }
  .product-line { font-family: "Quicksand", sans-serif; font-weight: 400; font-size: 17px; letter-spacing: 5.4px; fill: var(--lime); }
  .product-type { font-family: "Quicksand", sans-serif; font-weight: 300; font-size: 21px; fill: var(--lime); }
  .flavour-name { font-family: "Great Vibes", cursive; font-size: 30px; fill: var(--ink-white); }
  .volume { font-family: "Oswald", sans-serif; font-weight: 300; font-size: 17px; letter-spacing: 1px; fill: var(--ink-white); }
  .servings { font-family: "Oswald", sans-serif; font-weight: 300; font-size: 8px; letter-spacing: 1.4px; fill: var(--ink-white); }
  .side-claim { font-family: "Quicksand", sans-serif; font-weight: 400; font-size: 26px; fill: var(--ink-white); }
</style>
</head>
<body>
<svg class="bottle-art" viewBox="0 0 1200 900" xmlns="http://www.w3.org/2000/svg">
  <defs>
    <linearGradient id="body-fill" x1="0" y1="0" x2="0" y2="1">
      <stop offset="0" stop-color="var(--body-top)"/>
      <stop offset="1" stop-color="var(--body-bottom)"/>
    </linearGradient>
    <radialGradient id="liquid-fill" cx="0.45" cy="0.45" r="0.7">
      <stop offset="0" stop-color="var(--lime-light)"/>
      <stop offset="0.6" stop-color="var(--lime)"/>
      <stop offset="1" stop-color="var(--lime-deep)"/>
    </radialGradient>
    <radialGradient id="fruit-fill" cx="0.5" cy="0.5" r="0.55">
      <stop offset="0" stop-color="var(--kiwi-flesh)"/>
      <stop offset="1" stop-color="var(--kiwi-skin)"/>
    </radialGradient>
    <clipPath id="front-shape">
      <path d="M60,0 H252 C275,0 300,40 312,57 C308,120 300,170 300,220 C300,300 312,340 312,372 C300,400 280,428 252,428 H60 C32,428 12,400 0,372 C0,340 12,300 12,220 C12,170 4,120 0,57 C12,40 37,0 60,0 Z"/>
    </clipPath>
    <clipPath id="side-shape">
      <path d="M0,0 H62 C80,18 94,42 94,57 C92,120 86,170 86,220 C86,300 94,340 94,372 C88,396 76,414 62,428 H0 Z"/>
    </clipPath>
  </defs>

  <!-- Front face -->
  <g class="bottle-front" transform="translate(398,236)">
    <g clip-path="url(#front-shape)">
      <rect class="bottle-body" width="312" height="428" fill="url(#body-fill)"/>
      <line class="cap-seam" x1="0" y1="57" x2="312" y2="57" stroke="var(--seam)" stroke-width="1.5"/>
      <path class="cap-notch" d="M132,57 C140,44 172,44 180,57 C172,70 140,70 132,57 Z" fill="var(--seam)"/>
      <ellipse class="liquid-window" cx="-10" cy="338" rx="155" ry="116" fill="url(#liquid-fill)" role="img" aria-label="Window showing the bubbly lime-green kiwi liquid inside the bottle"/>
    </g>

    <g class="natural-claim">
      <text class="claim-figure" x="108" y="32">100%</text>
      <text class="claim-word" x="158" y="28">Natural</text>
      <text class="claim-sub" x="158" y="34">INGREDIENTS</text>
    </g>

    <text class="brand-name" x="156" y="152" text-anchor="middle">VEMO</text>

    <text class="product-line" x="79" y="206">Liquid Water</text>
    <text class="product-type" x="234" y="236" text-anchor="end">Enhancer</text>

    <text class="flavour-name" x="197" y="276" text-anchor="middle">Puply Kiwi</text>

    <ellipse class="fruit-picture" cx="222" cy="324" rx="62" ry="40" fill="url(#fruit-fill)" role="img" aria-label="Whole kiwi fruit and two kiwi halves with green leaves"/>

    <text class="volume" x="199" y="392" text-anchor="middle">60 ML</text>
    <text class="servings" x="199" y="408" text-anchor="middle">30 SERVINGS 6 FL OZ PER SERVING</text>
  </g>

  <!-- Side face -->
  <g class="bottle-side" transform="translate(722,236)">
    <g clip-path="url(#side-shape)">
      <rect class="bottle-body" width="94" height="428" fill="url(#body-fill)"/>
      <line class="cap-seam" x1="0" y1="57" x2="94" y2="57" stroke="var(--seam)" stroke-width="1.5"/>
      <path class="liquid-window" d="M0,224 C40,222 70,226 94,236 V428 H0 Z" fill="url(#liquid-fill)" role="img" aria-label="Window showing the bubbly lime-green kiwi liquid inside the bottle"/>
    </g>
    <text class="side-claim" transform="translate(44,200) rotate(-90)">Sugar Free</text>
  </g>
</svg>
</body>
</html>
```